Ironbark Shift Workforce

We are a underground coal mining labour hire company, needing a website that links into our online payroll (www.wagetrackly.com.au) and also need to have job applications page that is a preform with drop down menu,s with answers or check boxes. We would also need a 3 tier administration access for access to different files.
We are looking for an ongoing relationship with future app integration

Reason: There are a few more designs to come and I'm out at the mine for another week

Industry/Entity Type

Coal Mining

```html
<!DOCTYPE html>
<html lang="en">
<head>
<meta charset="utf-8">
<title>Ironbark Shift Workforce</title>
<link href="https://fonts.googleapis.com/css2?family=Open+Sans:wght@400;600&family=Exo:wght@400;500&display=swap" rel="stylesheet">
<style>
:root{
  --black:#000;
  --nav:#0d0d0d;
  --nav-active:#2b2b2b;
  --orange:#e0761a;
  --orange-dark:#b8540a;
  --page:#f6f6f6;
  --text:#333;
  --muted:#777;
  --rule:#dcdcdc;
  --band:#c9c9c9;
  --brand-blue:#3c3f9a;
}
*{margin:0;padding:0;box-sizing:border-box}
html,body{width:931px;height:1200px;overflow:hidden}
body{position:relative;background:var(--page);font-family:"Open Sans",sans-serif;color:var(--text)}
.abs{position:absolute}
.header{left:0;top:0;width:931px;height:158px;background:var(--black)}
.brand-mark{left:163px;top:10px;width:90px;height:100px;border-radius:50%;background:radial-gradient(circle,#e8761c 0%,#7a3a0c 55%,#000 75%)}
.brand-name{left:182px;top:122px;color:#fff;font:600 13px "Open Sans",sans-serif;display:flex;align-items:center;gap:4px}
.brand-name i{width:15px;height:15px;border-radius:50%;background:#fff;display:inline-block}
.social{left:630px;top:14px;display:flex;gap:6px}
.social span{width:27px;height:27px;border-radius:50%;border:1.5px solid #3a3a3a}
.phone{left:627px;top:80px;display:flex;align-items:center;gap:9px}
.phone-icon{width:42px;height:40px;border-radius:50%;border:1.5px solid #3a3a3a;display:flex;align-items:center;justify-content:center}
.phone-num{color:#5a5a5a;font:300 22px "Open Sans",sans-serif;letter-spacing:.5px}
.nav{left:0;top:158px;width:931px;height:30px;background:var(--nav);border-bottom:2px solid var(--orange);height:32px}
.nav ul{list-style:none;display:flex;position:absolute;left:134px;top:0;height:30px}
.nav li{color:#fff;font-size:10px;line-height:30px;padding:0 14.5px}
.nav li.active{background:var(--nav-active)}
.slider{left:134px;top:206px;width:665px;height:332px;background:#000;padding:4px}
.slider-shadow{left:150px;top:530px;width:630px;height:30px;border-radius:50%;box-shadow:0 14px 18px -8px rgba(0,0,0,.45)}
.slide-photo{width:100%;height:100%;background:linear-gradient(160deg,#8a8a88 0%,#5d5c58 40%,#3a3936 70%,#6b6b69 100%);position:relative}
.slide-caption{left:1px;top:210px;height:38px;padding:0 12px;background:rgba(20,20,20,.75);color:#fff;font:400 19px "Exo",sans-serif;line-height:38px}
.slide-arrow{top:172px;width:12px;height:12px;border-radius:50%;background:rgba(255,255,255,.5)}
.dots{left:302px;top:308px;display:flex;gap:8px}
.dots span{width:8px;height:8px;border-radius:50%;background:#fff}
.dots span.ring{background:none;border:1.5px solid #fff}
.welcome-title{left:141px;top:589px;font:500 15px "Exo",sans-serif;color:#222}
.welcome-text{left:146px;top:619px;width:440px;font-size:9.6px;line-height:20px;color:#444}
.welcome-text p+p{margin-top:5px}
.frame{background:#fff;border:1px solid #ddd;padding:3px;box-shadow:0 1px 2px rgba(0,0,0,.08)}
.frame div{width:100%;height:100%}
.divider{left:134px;top:775px;width:652px;height:1px;background:var(--rule)}
.col-title{top:798px;font:500 12px "Exo",sans-serif;color:#222}
.pager{top:801px;display:flex;gap:4px}
.pager span{width:10px;height:10px;border-radius:50%;border:1px solid #888}
.col-text{top:938px;width:205px;font-size:8.7px;line-height:16px;color:#444}
.btn{top:1027px;width:78px;height:23px;border-radius:2px;background:linear-gradient(#e5801f,var(--orange-dark));color:#fff;font-size:8.5px;text-align:center;line-height:23px;box-shadow:0 2px 2px rgba(0,0,0,.2)}
.news{left:360px;top:822px;width:204px;list-style:none}
.news li{border-bottom:1px solid var(--rule);padding:6px 2px 8px}
.news li+li{padding-top:13px}
.news h4{font:400 9.3px "Open Sans",sans-serif;color:#222}
.news small{display:block;font-size:6px;color:#666;margin-top:5px}
.band{left:0;top:1075px;width:931px;height:60px;background:var(--band)}
.band-label{left:141px;top:1096px;font:400 13px "Exo",sans-serif;color:#222}
.email{left:254px;top:1094px;width:204px;height:24px;background:#d8d8d8;border:1px solid #d0d0d0;font-size:7.5px;color:#999;padding-left:7px;line-height:22px}
.subscribe{left:467px;top:1095px;width:99px;height:22px;background:linear-gradient(#e5801f,var(--orange-dark));color:#fff;font-size:10px;text-align:center;line-height:22px}
.band-rule{left:608px;top:1077px;height:57px;border-left:1px dotted #555}
.partner{left:638px;top:1090px;display:flex;align-items:center;gap:6px;color:var(--brand-blue);font:400 23px "Open Sans",sans-serif;letter-spacing:-.3px}
.partner i{width:20px;height:20px;background:var(--brand-blue);display:inline-block}
.footer{left:0;top:1135px;width:931px;height:65px;background:var(--black);color:#ddd;text-align:center}
.footer-links{padding-top:16px;font-size:7.8px}
.footer-links span{padding:0 4px}
.copyright{margin-top:16px;font-size:7.5px;color:#aaa}
</style>
</head>
<body>
<header class="header abs">
  <div class="brand-mark abs" role="img" aria-label="Ironbark Shift Workforce emblem artwork"></div>
  <div class="brand-name abs"><i></i>ISW</div>
  <div class="social abs" aria-label="Social links"><span></span><span></span><span></span><span></span><span></span></div>
  <div class="phone abs">
    <div class="phone-icon"><svg width="20" height="20" viewBox="0 0 24 24"><path d="M6.6 10.8a15 15 0 0 0 6.6 6.6l2.2-2.2c.3-.3.7-.4 1-.2 1.1.4 2.3.6 3.6.6.6 0 1 .4 1 1V20c0 .6-.4 1-1 1A17 17 0 0 1 3 4c0-.6.4-1 1-1h3.5c.6 0 1 .4 1 1 0 1.3.2 2.5.6 3.6.1.3 0 .7-.2 1z" fill="#3a3a3a"/></svg></div>
    <div class="phone-num">123 456 789</div>
  </div>
</header>
<nav class="nav abs">
  <ul><li class="active">Home</li><li>Apply for position</li><li>Pay Portal</li><li>Download</li><li>Mission</li><li>About us</li><li>Contact us</li></ul>
</nav>
<div class="slider-shadow abs"></div>
<section class="slider abs">
  <div class="slide-photo" role="img" aria-label="Haul truck and excavator working an open cut coal face">
    <div class="slide-caption abs">Ironbark Shift Workforce</div>
    <div class="slide-arrow abs" style="left:4px"></div>
    <div class="slide-arrow abs" style="right:4px"></div>
    <div class="dots abs"><span></span><span class="ring"></span><span></span><span></span></div>
  </div>
</section>
<h1 class="welcome-title abs">Welcome To Ironbark Shift Workforce</h1>
<div class="welcome-text abs">
  <p>We are KRTM pty ltd trading as Ironbark Shift Workforce,&nbsp; we are experienced in ground consolidation in underground coal mines,&nbsp; in short when they collapse or cave in we come in with chemical pumps and stabilise the ground or fill cavities which will then allow for the mining process to continue. We also do general mine labor as well.</p>
  <p>We are a labor hire company for major mining services company,&nbsp; we offer labor solutions in New South Wales and Queensland in the underground coal mines.</p>
</div>
<div class="frame abs" style="left:587px;top:602px;width:200px;height:138px"><div role="img" aria-label="Mine workers in hi-vis gear underground" style="background:linear-gradient(120deg,#3b3530,#7b6a3a 45%,#c9c23a 70%,#4a4238)"></div></div>
<div class="divider abs"></div>

<h2 class="col-title abs" style="left:141px">Services</h2>
<div class="frame abs" style="left:144px;top:826px;width:200px;height:105px"><div role="img" aria-label="Underground drilling rig with crew" style="background:linear-gradient(135deg,#2a2220,#7a3a22 40%,#8c7a52 65%,#2d2a28)"></div></div>
<p class="col-text abs" style="left:146px">Eu ipsum. Quisque aliquam mollis pede praesent elementum semper aliquam cum porttitor fusce consectetuer. Pharetra, lobortis nisi fusce moles- tie donec donec porttitor. Metus at auctor facilisis rutrum, dolor bibendum...</p>
<div class="btn abs" style="left:146px">Learn more</div>

<h2 class="col-title abs" style="left:360px">Latest News</h2>
<div class="pager abs" style="left:539px"><span></span><span></span></div>
<ul class="news abs">
  <li><h4>CREW UP FOR 2 SAFETY AWARDS FOR 2...</h4><small>Comments (1), 06-04-2012</small></li>
  <li><h4>NOBIS HOMERO INVIDUNT PER IN, ...</h4><small>Comments (1), 06-04-2012</small></li>
  <li><h4>NIGHT CREW SCORING 'BLUE SEAM...</h4><small>Comments (1), 06-04-2012</small></li>
  <li><h4>CU IUS CONVENIRE DISPUTANDO, A...</h4><small>Comments (1), 06-04-2012</small></li>
</ul>
<div class="btn abs" style="left:365px">Learn more</div>

<h2 class="col-title abs" style="left:578px">Our Blog</h2>
<div class="pager abs" style="left:755px"><span></span><span></span></div>
<div class="frame abs" style="left:582px;top:826px;width:198px;height:105px"><div role="img" aria-label="Site crew in orange vests at a ground breaking" style="background:linear-gradient(180deg,#b9d3e6 0%,#d9d9d2 35%,#e3762a 60%,#6d6a5a 100%)"></div></div>
<p class="col-text abs" style="left:583px;width:205px">Eu ipsum. Quisque aliquam mollis pede praesent elementum semper aliquam cum porttitor fusce consectetuer. Pharetra, lobortis nisi fusce moles- tie donec donec porttitor. Metus at auctor facilisis rutrum, dolor bibendum...</p>
<div class="btn abs" style="left:583px">Learn more</div>

<section class="band abs"></section>
<div class="band-label abs">Newsletter Signup :</div>
<div class="email abs">Enter Your Email Address</div>
<div class="subscribe abs">Subscribe</div>
<div class="band-rule abs"></div>
<div class="partner abs"><i></i>wagetrackly</div>

<footer class="footer abs">
  <div class="footer-links"><span>Login</span>|<span>Privacy Policy</span>|<span>Terms &amp; Conditions</span>|<span>Mining Services</span>|<span>Sitemap</span>|<span>Contact Us</span></div>
  <div class="copyright">copyright @ 2014 ironbarkshift. All Right Reserved.</div>
</footer>
</body>
</html>
```